New Service Brochure for The Brackenford Spa

Hi All! We are looking for a new brochure design- tri-fold, double sided, and full color. We are a certified Tovrel Spa for men and women in the heart of the Catskill Mountains of upstate New York. Our clients would describe us as laid back luxury with no pretensions and a home away from home vibe. Our font is Avalon. Key colors are black, white and gold. Looking for an inviting, clean, and modern/minimalist spread with a touch of elegance. No orchid imagery, please. I would like our "Tovrel Spa" logo on cover, too please. Front cover image with with logo and "Tovrel Spa" Sticker . Bottom of back with contact info. We would prefer massages go on left inside page, facials in middle and right inside, nails on back left, but we are open to new or different layout proposals. Thank you!

Target Market(s)

Men & Women.

Industry/Entity Type

Health And Wellness

Font styles to use
Other font styles liked:
• Avalon is our signature font

Requirements
Must have
• Easy on the eyes.
Nice to have
• Negative space.
Should not have
• No orchids. Busy lines and wild colors.

```html
<!DOCTYPE html>
<html lang="en">
<head>
<meta charset="utf-8">
<title>The Brackenford Spa – Tri-fold Brochure</title>
<link href="https://fonts.googleapis.com/css2?family=Raleway:wght@300;400;500;600&display=swap" rel="stylesheet">
<style>
:root{
  --stage:#2e2e2e;
  --paper:#f7f6f3;
  --paper-shade:#ecebe7;
  --ink:#3a3a3a;
  --ink-soft:#6a6a6a;
  --gold:#d3a435;
  --gold-soft:#e2c27a;
  --gold-pale:#efdcae;
}
*{box-sizing:border-box;margin:0;padding:0}
html,body{width:800px;height:1200px;overflow:hidden}
body{background:var(--stage);font-family:"Raleway",sans-serif;color:var(--ink);position:relative}
.spread{position:absolute;left:40px;width:720px;height:557px;display:flex;box-shadow:0 10px 30px rgba(0,0,0,.45)}
.spread--outside{top:30px}
.spread--inside{top:613px}
.panel{position:relative;width:240px;height:100%;background:var(--paper);overflow:hidden}
.panel + .panel{border-left:1px solid var(--paper-shade)}
.art{position:absolute;left:0;width:240px}
.gold{color:var(--gold)}
.rule{display:block;width:60px;height:1px;background:var(--gold);margin:8px auto;position:relative}
.rule::after{content:"";position:absolute;left:27px;top:-2px;width:5px;height:5px;border-radius:50%;background:var(--gold)}
.body-copy{font-size:8.5px;line-height:1.45;color:var(--ink-soft)}

/* outside left */
.wellness{position:absolute;left:26px;top:34px;right:24px}
.wellness h2{font-weight:300;font-size:22px;letter-spacing:1px;line-height:1.05}
.wellness h2 span{display:block}
.wellness p{margin-top:10px}
.located{position:absolute;left:26px;right:20px;bottom:46px;font-weight:300;font-size:16px;line-height:1.35;color:var(--ink)}

/* outside middle */
.contact{position:absolute;top:262px;left:0;right:0;text-align:center}
.contact h2{font-weight:300;font-size:22px}
.contact-list{list-style:none;margin-top:12px;font-size:9.5px;line-height:1.5;color:var(--ink-soft)}
.contact-list li{margin-bottom:7px;display:flex;justify-content:center;gap:6px;align-items:flex-start}
.contact-list svg{flex:none;margin-top:2px}
.social{display:flex;justify-content:center;align-items:center;gap:8px;margin-top:10px}
.social .line{width:40px;height:1px;background:var(--gold-soft)}
.social .dot{width:14px;height:14px;border-radius:50%;background:var(--gold)}

/* outside right / cover */
.brand{position:absolute;top:30px;left:0;right:0;text-align:center}
.brand-name{font-weight:400;font-size:22px;letter-spacing:1px;color:var(--ink);line-height:1.1}
.brand-tag{font-size:8px;color:var(--ink-soft);margin-top:5px;letter-spacing:.3px}
.badge{position:absolute;left:34px;top:270px;display:flex;flex-direction:column;align-items:center;gap:4px}
.badge .seal{width:34px;height:34px;border-radius:50%;background:#3d6b3a}
.badge span{font-size:7px;font-weight:500;color:var(--ink)}
.slogan{position:absolute;top:292px;right:26px;text-align:right;font-weight:300;font-size:19px;line-height:1.2}
.slogan .rule{margin:10px 0 0 auto}
.url{position:absolute;top:372px;right:26px;font-size:9px;letter-spacing:1.5px;color:var(--ink)}

/* inside */
.section-title{font-weight:500;font-size:19px;letter-spacing:1px;color:var(--gold);text-align:center}
.intro{text-align:center;margin:4px 24px 0;font-size:8.5px}
.menu{list-style:none;margin:14px 22px 0}
.menu li{margin-bottom:15px}
.menu .row{display:flex;justify-content:space-between;align-items:baseline}
.menu h3{font-weight:500;font-size:12px;color:var(--gold)}
.menu .price{font-size:11px;font-weight:500;color:var(--ink)}
.menu p{font-size:7.5px;line-height:1.4;color:var(--ink-soft);margin-top:3px}
.menu p em{font-style:normal;color:var(--gold)}
.massages{padding-top:34px}
.services{padding-top:26px}
.services .menu{margin-top:0}
.feature{text-align:center;margin:4px 0 14px}
.feature small{display:block;font-size:14px;color:var(--gold);font-weight:500;letter-spacing:1px}
.feature strong{display:block;font-size:16px;font-weight:400;letter-spacing:1px;color:var(--ink)}
.extras{padding:34px 24px 0;text-align:center}
.extras p{font-size:8.5px;line-height:1.45;color:var(--ink-soft);margin-top:6px}
.extras .call{font-size:11px;color:var(--ink);margin-top:6px;line-height:1.35}
.extras .call span{color:var(--gold)}
.extras .section-title + .rule{margin:6px auto}
.gift{margin-top:26px}
</style>
</head>
<body>

<!-- Outside spread -->
<section class="spread spread--outside" aria-label="Brochure outside">
  <article class="panel">
    <div class="wellness">
      <h2><span>WELLNESS</span><span class="gold">REDEFINED</span></h2>
      <p class="body-copy">We believe the simple luxuries of life and service come with a heartfelt smile, a warm cup of tea, and fresh air. Not to mention wide open spaces, breath-taking views and the number one organic skin care line in the world.</p>
    </div>
    <svg class="art" style="top:170px" width="240" height="170" viewBox="0 0 240 170">
      <g role="img" aria-label="Massage stones with a rosemary sprig and a bottle of oil">
        <defs><linearGradient id="stones" x1="0" y1="0" x2="1" y2="1"><stop offset="0" stop-color="#eeeeec"/><stop offset=".6" stop-color="#8a8c86"/><stop offset="1" stop-color="#3c3c3a"/></linearGradient></defs>
        <path d="M0 0H240V100C170 130 90 150 0 120Z" fill="url(#stones)"/>
      </g>
      <path d="M0 120C90 150 170 130 240 100V128C170 150 90 168 0 146Z" fill="var(--gold-soft)"/>
      <path d="M0 146C90 168 170 150 240 128V136C170 160 90 170 0 156Z" fill="var(--gold-pale)"/>
    </svg>
    <p class="located">Located in the heart of the Catskill Mountains, our down-to-earth staff, laid back atmosphere, and extraordinary services leave no room for pretenses.</p>
  </article>

  <article class="panel">
    <svg class="art" style="top:0" width="240" height="240" viewBox="0 0 240 240">
      <g role="img" aria-label="Spa stones, salt bowl, candles and rose petals on a wooden tray">
        <defs><linearGradient id="tray" x1="0" y1="0" x2="1" y2="1"><stop offset="0" stop-color="#f2f0ec"/><stop offset=".5" stop-color="#d9b88c"/><stop offset="1" stop-color="#eedfe0"/></linearGradient></defs>
        <path d="M0 0H240V200C170 190 90 230 0 220Z" fill="url(#tray)"/>
      </g>
      <path d="M0 220C90 230 170 190 240 200V214C170 206 90 240 0 236Z" fill="var(--gold-soft)"/>
    </svg>
    <div class="contact">
      <h2>Contact Us</h2>
      <span class="rule"></span>
      <ul class="contact-list">
        <li><svg width="8" height="10" viewBox="0 0 8 10"><path d="M4 0A4 4 0 0 1 8 4C8 7 4 10 4 10S0 7 0 4A4 4 0 0 1 4 0Z" fill="var(--gold)"/><circle cx="4" cy="4" r="1.5" fill="#fff"/></svg><span>22 Alder Hollow Road<br>Brackenford, NY 12400<br>Right off Main Street</span></li>
        <li><svg width="10" height="8" viewBox="0 0 10 8"><rect x=".5" y=".5" width="9" height="7" fill="none" stroke="var(--gold)"/><path d="M.5 .5L5 4.5 9.5 .5" fill="none" stroke="var(--gold)"/></svg><span>info@BrackenfordSpa.com</span></li>
        <li><svg width="9" height="9" viewBox="0 0 9 9"><circle cx="4.5" cy="4.5" r="4.5" fill="var(--gold)"/><path d="M3 2.5L4 4 3.6 4.6C4 5.4 4.6 6 5.3 6.3L5.9 5.9 7 6.8 6.3 7.4C4.4 7.2 2 4.8 1.9 3Z" fill="#fff"/></svg><span>(518) 555-0142</span></li>
        <li><svg width="9" height="9" viewBox="0 0 9 9"><circle cx="4.5" cy="4.5" r="4" fill="none" stroke="var(--gold)"/><path d="M.5 4.5H8.5M4.5 .5C2.5 3 2.5 6 4.5 8.5M4.5 .5C6.5 3 6.5 6 4.5 8.5" fill="none" stroke="var(--gold)" stroke-width=".7"/></svg><span>www.brackenfordspa.com</span></li>
      </ul>
      <div class="social"><span class="line"></span><span class="dot"></span><span class="dot"></span><span class="dot"></span><span class="line"></span></div>
    </div>
  </article>

  <article class="panel">
    <div class="brand">
      <p class="brand-name">THE BRACKENFORD<br>SPA</p>
      <p class="brand-tag">a boutique spa for Men &amp; Women</p>
    </div>
    <svg class="art" style="top:105px" width="240" height="150" viewBox="0 0 240 150">
      <g role="img" aria-label="Woman relaxing on a massage table">
        <defs><linearGradient id="guest" x1="0" y1="0" x2="1" y2="0"><stop offset="0" stop-color="#d8e3e6"/><stop offset=".5" stop-color="#e8cdb8"/><stop offset="1" stop-color="#f4f4f2"/></linearGradient></defs>
        <path d="M30 0H240V95C170 110 110 130 30 118Z" fill="url(#guest)"/>
      </g>
      <path d="M30 118C110 130 170 110 240 95V112C170 128 100 150 20 130Z" fill="var(--gold-soft)"/>
    </svg>
    <div class="badge"><span class="seal"></span><span>Tovrel Spa</span></div>
    <div class="slogan">Escape<br>the congestion of<br>everyday life<span class="rule"></span></div>
    <p class="url">www.brackenfordspa.com</p>
  </article>
</section>

<!-- Inside spread -->
<section class="spread spread--inside" aria-label="Brochure inside">
  <article class="panel massages">
    <h2 class="section-title">MASSAGES</h2>
    <span class="rule"></span>
    <p class="intro body-copy">Tired, sore muscles, and exhausted minds are refreshed by the perfect massage customized to your individual needs.</p>
    <ul class="menu">
      <li><div class="row"><h3>Swedish Massage</h3><span class="price">$105/$160</span></div><p>Relaxing and therapeutic. Ease tension and enhance circulation. Great for a first time massage or any spa veteran. <em>55 or 90 minutes.</em></p></li>
      <li><div class="row"><h3>Deep Tissue</h3><span class="price">$115/$175</span></div><p>A therapeutic combination of slow and deep pressure alleviates chronic pain, muscle fatigue, and limited range of motion. Muscle therapy lotion or creme. <em>55 or 90 minutes.</em></p></li>
      <li><div class="row"><h3>Tension Tamer</h3><span class="price">$125/$195</span></div><p>Head, neck and shoulders. Deep tissue with hot towels, muscle soothing oils, and cupping. <em>55 or 90 minutes.</em></p></li>
      <li><div class="row"><h3>Hot Stone</h3><span class="price">$175</span></div><p>Unforgettable. Warm basalt lava stones melt away all stress and tension in sore muscles and joints. The ultimate après ski treat. <em>90 minutes.</em></p></li>
      <li><div class="row"><h3>Recovery</h3><span class="price">$110/$170</span></div><p>Specific to your athletic needs, whether pro or a weekend warrior. Relax, stretch and recover. <em>55 or 90 minutes.</em></p></li>
    </ul>
  </article>

  <article class="panel services">
    <ul class="menu">
      <li><div class="row"><h3>Compression Rapid Recovery</h3><span class="price">$135</span></div><p>Recover faster and feel better while optimizing your massage time with our compression boots. Gentle wave pressure moves fluid, speeds recovery and eases tired legs on the go. <em>55 minutes.</em></p></li>
      <li><div class="row"><h3>Prenatal</h3><span class="price">$110</span></div><p>Ultimate treat for mother-to-be. Soothes aches and pains during pregnancy. Mother must be out of first trimester. <em>55 minutes.</em></p></li>
      <li><div class="row"><h3>Couples</h3><span class="price">$210 &amp;up</span></div><p>For lovebirds or loved ones. Relax and recoup with your favorite person. <em>55 or 90 minutes.</em></p></li>
    </ul>
    <div class="feature"><small>FEATURE</small><strong>MASSAGE SERVICES</strong></div>
    <ul class="menu">
      <li><div class="row"><h3>Aromatherapy</h3><span class="price">$115/$170</span></div><p>Speak to your massage therapist about our weekly aromatherapy blends, curated from around the world and blended in house. <em>55 or 90 minutes.</em></p></li>
      <li><div class="row"><h3>Calm Down and Relax</h3><span class="price">$135/$175</span></div><p>Calm down and relax your mind and body. Decompress with your choice of seasonal aromatherapy blends and hot stones. <em>55 or 90 minutes.</em></p></li>
      <li><div class="row"><h3>Green Tea and Peppermint Massage</h3><span class="price">$115/$170</span></div><p>Perfect for strained and tired muscles and joints. Combines green tea and mint to boost circulation and leave you refreshed. <em>55 or 90 minutes.</em></p></li>
    </ul>
  </article>

  <article class="panel extras">
    <h2 class="section-title">SPA PARTIES</h2>
    <span class="rule"></span>
    <p>Perfect for bridal showers, birthday parties and any time you want to host a unique and extraordinary experience.</p>
    <p class="call"><span>Call (518) 555-0142</span> for more information and booking.</p>
    <h2 class="section-title gift">GIFT CERTIFICATES</h2>
    <span class="rule"></span>
    <p>Birthdays, holidays, and beyond! Sometimes it's nice to get an unexpected gift that says "you should take some time for yourself."</p>
    <p class="call"><span>Call (518) 555-0142</span> and we'll help you pick the perfect gift for any occasion or <span>purchase directly online.</span></p>
    <svg class="art" style="left:0;bottom:0" width="240" height="130" viewBox="0 0 240 130">
      <g role="img" aria-label="Towel, oil bottles and an herbal compress on a wooden tray">
        <defs><radialGradient id="gift" cx=".6" cy=".5" r=".6"><stop offset="0" stop-color="#efe2b6"/><stop offset=".7" stop-color="#e9e4d8"/><stop offset="1" stop-color="#f7f6f3"/></radialGradient></defs>
        <rect x="40" y="0" width="200" height="130" fill="url(#gift)"/>
      </g>
    </svg>
  </article>
</section>

</body>
</html>
```